3 Business Card designs for a company with multiple services

We are a company that has 3 main services:

1) Security - CCTV & Alarm Sepcialists
2) Broadcast - Broadcast Sales and Technical Services
3) Distribution - Quality Products, Quality Service

The broadcast service is for Video Broadcast.

I will include our logos for each service.

I would like to also create a business card design for 7QK in general (see main logo).

Each card will be two-sided. On the front I would think it would include Logo, Name, Posistion and Mobile (and possibly email). And possibly our main number (which may be something like 1800 639 415)

On the back it MUST include a "lined" section to be able to write short quotes / prices.

Then include more details like Phone: 1800 639 415 Fax: 1800 639 412 Postal: PO Box 731, Tallowen, QLD Australia 4290 Website: www.7qk.com.au

We would like a fresh, inovative card design with that "wow check this out" feel about it.

Look forward to seeing what you can do! :)

Corey

Industry/Entity Type

Business

Requirements
Must have
• Quote section on the back!
Editable files.

```html
<!DOCTYPE html>
<html lang="en">
<head>
<meta charset="utf-8">
<title>7QK Business Cards</title>
<link href="https://fonts.googleapis.com/css2?family=Arimo:wght@400;700&display=swap" rel="stylesheet">
<style>
  :root{
    --page-bg:#3a3a3a;
    --card-white:#f4f4f4;
    --line-grey:#9a9a9a;
    --ink-dark:#3c3c3c;
    --strip-dark:#2e2e2e;
    --accent-orange:#e8701a;
    --text-light:#ffffff;
    --red-main:#d01e0a;
    --red-deep:#a80d04;
    --red-flap:#bb1606;
    --red-bg:#6e0f24;
    --amber-main:#f0a012;
    --amber-deep:#d87c06;
    --amber-flap:#e08b04;
    --amber-bg:#6f6310;
    --blue-main:#1f4fc4;
    --blue-deep:#0f2f8e;
    --blue-flap:#1a44b0;
    --blue-bg:#0d5a74;
  }
  *{margin:0;padding:0;box-sizing:border-box}
  html,body{width:1200px;height:2642px;overflow:hidden}
  body{font-family:'Arimo',Arial,sans-serif;background:var(--page-bg);display:grid;grid-template-rows:repeat(3,1fr);gap:6px}
  .panel{position:relative;display:flex;align-items:center;justify-content:center;gap:60px}
  .panel--security{background:var(--red-bg);--c-main:var(--red-main);--c-deep:var(--red-deep);--c-flap:var(--red-flap)}
  .panel--broadcast{background:var(--amber-bg);--c-main:var(--amber-main);--c-deep:var(--amber-deep);--c-flap:var(--amber-flap)}
  .panel--distribution{background:var(--blue-bg);--c-main:var(--blue-main);--c-deep:var(--blue-deep);--c-flap:var(--blue-flap)}

  .card{position:relative;width:520px;height:310px;border-radius:18px;overflow:hidden;box-shadow:0 10px 24px rgba(0,0,0,.45)}
  .card svg{position:absolute;inset:0;width:100%;height:100%}

  /* front */
  .card-front{background:linear-gradient(160deg,var(--c-main),var(--c-deep))}
  .card-front .flap-main{fill:var(--c-flap)}
  .card-front .flap-edge{fill:none;stroke:rgba(0,0,0,.18);stroke-width:1.5}
  .card-front .texture{position:absolute;left:120px;top:110px;width:230px;height:170px;border-radius:50%;
    background:radial-gradient(ellipse at center,rgba(255,255,255,.22),rgba(255,255,255,0) 70%)}
  .front-info{position:absolute;right:46px;top:100px;width:250px;color:var(--text-light);text-align:right}
  .brand{display:flex;align-items:center;justify-content:flex-end;gap:8px}
  .brand-mark{width:28px;height:28px;background:var(--text-light);opacity:.9;border-radius:4px}
  .brand-name{font-weight:700;font-size:32px;letter-spacing:6px;color:var(--text-light)}
  .service-name{font-weight:700;font-size:11px;letter-spacing:3px;margin-top:4px}
  .holder-name{font-size:15px;margin-top:30px;letter-spacing:.5px}
  .rule{height:1px;background:rgba(255,255,255,.55);margin:8px 0 6px}
  .holder-detail{font-size:11px;line-height:1.4}

  /* back */
  .card-back{background:var(--card-white)}
  .card-back .flap-line{fill:none;stroke:#c9c9c9;stroke-width:2}
  .card-back .quote-line{stroke:var(--line-grey);stroke-width:1}
  .back-info{position:absolute;left:250px;top:196px;width:245px;color:var(--ink-dark)}
  .service-strip{display:flex;align-items:center;justify-content:space-between;background:var(--strip-dark);height:30px;padding:0 10px;color:var(--text-light)}
  .service-strip .services{font-size:7.5px;font-weight:700;letter-spacing:1px}
  .service-strip .strip-brand{display:flex;align-items:center;gap:5px;font-weight:700;font-size:17px;letter-spacing:3px}
  .service-strip .strip-mark{width:12px;height:12px;background:var(--text-light)}
  .contact{font-size:11px;line-height:1.45;margin-top:8px}
  .contact .label{color:var(--accent-orange)}
</style>
</head>
<body>

  <section class="panel panel--security">
    <article class="card card-front">
      <svg viewBox="0 0 520 310" aria-hidden="true">
        <polygon class="flap-main" points="0,0 190,85 330,0"/>
        <polygon class="flap-main" points="300,0 390,60 520,0"/>
        <polyline class="flap-edge" points="0,0 190,85 330,0"/>
        <polyline class="flap-edge" points="300,0 390,60 520,0"/>
      </svg>
      <div class="texture" role="img" aria-label="Soft abstract light streaks texture"></div>
      <div class="front-info">
        <div class="brand"><span class="brand-mark"></span><span class="brand-name">7QK</span></div>
        <div class="service-name">SECURITY</div>
        <div class="holder-name">LOREM IPSUM DOLOR</div>
        <div class="rule"></div>
        <div class="holder-detail">Manager<br>123.4567.890 ||| 1800 639 415<br>LoremIpsumDolor@7qk.com</div>
      </div>
    </article>
    <article class="card card-back">
      <svg viewBox="0 0 520 310" aria-hidden="true">
        <polyline class="flap-line" points="0,0 190,85 360,0"/>
        <line class="quote-line" x1="250" y1="70" x2="495" y2="70"/>
        <line class="quote-line" x1="250" y1="92" x2="495" y2="92"/>
        <line class="quote-line" x1="250" y1="114" x2="495" y2="114"/>
        <line class="quote-line" x1="250" y1="136" x2="495" y2="136"/>
        <line class="quote-line" x1="250" y1="158" x2="495" y2="158"/>
        <line class="quote-line" x1="250" y1="180" x2="495" y2="180"/>
      </svg>
      <div class="back-info">
        <div class="service-strip"><span class="services">SECURITY · BROADCAST · DISTRIBUTION</span><span class="strip-brand"><span class="strip-mark"></span>7QK</span></div>
        <div class="contact">1800 639 415 Fax: 1800 639 412<br>PO Box 731, Tallowen, QLD Australia 4290<br><span class="label">Website:</span> www.7qk.com.au</div>
      </div>
    </article>
  </section>

  <section class="panel panel--broadcast">
    <article class="card card-front">
      <svg viewBox="0 0 520 310" aria-hidden="true">
        <polygon class="flap-main" points="0,0 190,85 330,0"/>
        <polygon class="flap-main" points="300,0 390,60 520,0"/>
        <polyline class="flap-edge" points="0,0 190,85 330,0"/>
        <polyline class="flap-edge" points="300,0 390,60 520,0"/>
      </svg>
      <div class="texture" role="img" aria-label="Soft abstract light streaks texture"></div>
      <div class="front-info">
        <div class="brand"><span class="brand-mark"></span><span class="brand-name">7QK</span></div>
        <div class="service-name">BROADCAST</div>
        <div class="holder-name">LOREM IPSUM DOLOR</div>
        <div class="rule"></div>
        <div class="holder-detail">Manager<br>123.4567.890 ||| 1800 639 415<br>LoremIpsumDolor@7qk.com</div>
      </div>
    </article>
    <article class="card card-back">
      <svg viewBox="0 0 520 310" aria-hidden="true">
        <polyline class="flap-line" points="0,0 190,85 360,0"/>
        <line class="quote-line" x1="250" y1="70" x2="495" y2="70"/>
        <line class="quote-line" x1="250" y1="92" x2="495" y2="92"/>
        <line class="quote-line" x1="250" y1="114" x2="495" y2="114"/>
        <line class="quote-line" x1="250" y1="136" x2="495" y2="136"/>
        <line class="quote-line" x1="250" y1="158" x2="495" y2="158"/>
        <line class="quote-line" x1="250" y1="180" x2="495" y2="180"/>
      </svg>
      <div class="back-info">
        <div class="service-strip"><span class="services">SECURITY · BROADCAST · DISTRIBUTION</span><span class="strip-brand"><span class="strip-mark"></span>7QK</span></div>
        <div class="contact">1800 639 415 Fax: 1800 639 412<br>PO Box 731, Tallowen, QLD Australia 4290<br><span class="label">Website:</span> www.7qk.com.au</div>
      </div>
    </article>
  </section>

  <section class="panel panel--distribution">
    <article class="card card-front">
      <svg viewBox="0 0 520 310" aria-hidden="true">
        <polygon class="flap-main" points="0,0 190,85 330,0"/>
        <polygon class="flap-main" points="300,0 390,60 520,0"/>
        <polyline class="flap-edge" points="0,0 190,85 330,0"/>
        <polyline class="flap-edge" points="300,0 390,60 520,0"/>
      </svg>
      <div class="texture" role="img" aria-label="Soft abstract light streaks texture"></div>
      <div class="front-info">
        <div class="brand"><span class="brand-mark"></span><span class="brand-name">7QK</span></div>
        <div class="service-name">DISTRIBUTION</div>
        <div class="holder-name">LOREM IPSUM DOLOR</div>
        <div class="rule"></div>
        <div class="holder-detail">Manager<br>123.4567.890 ||| 1800 639 415<br>LoremIpsumDolor@7qk.com</div>
      </div>
    </article>
    <article class="card card-back">
      <svg viewBox="0 0 520 310" aria-hidden="true">
        <polyline class="flap-line" points="0,0 190,85 360,0"/>
        <line class="quote-line" x1="250" y1="70" x2="495" y2="70"/>
        <line class="quote-line" x1="250" y1="92" x2="495" y2="92"/>
        <line class="quote-line" x1="250" y1="114" x2="495" y2="114"/>
        <line class="quote-line" x1="250" y1="136" x2="495" y2="136"/>
        <line class="quote-line" x1="250" y1="158" x2="495" y2="158"/>
        <line class="quote-line" x1="250" y1="180" x2="495" y2="180"/>
      </svg>
      <div class="back-info">
        <div class="service-strip"><span class="services">SECURITY · BROADCAST · DISTRIBUTION</span><span class="strip-brand"><span class="strip-mark"></span>7QK</span></div>
        <div class="contact">1800 639 415 Fax: 1800 639 412<br>PO Box 731, Tallowen, QLD Australia 4290<br><span class="label">Website:</span> www.7qk.com.au</div>
      </div>
    </article>
  </section>

</body>
</html>
```